Social Media Graphics - Copperfield Loop

Create 6-7 individual social media graphics (square size) to encourage folks to join our online course, using either of the text below (only one set of text per graphic:

The Lantern Ridge Method
How to Create a 7-Figure Business From Scratch
Sign Up Today!

Or

The Lantern Ridge Method
Fast-track Your Way to a Multi-Million Business!
Sign Up Today!

For the color scheme of the graphics, use 1 or 2 colors in the color palette attached; or use any colors that look nice with their outfits; AVOID using red, white and blue altogether because it will look like an Independence Day (4th of July) graphic and we don’t want that; make sure the graphics appeal to both men and women

Make sure each graphic contains 1 of the 2 pics attached; and make sure one of the graphics is all TEXT only.

Target Market(s)

men and women looking to make more money

Industry/Entity Type

entrepreneurship

Requirements
Must have
• see the text document attached
Nice to have
• We are open to a nice color design; the color palette colors are not required, especially we don't want red, white and blue used together
Should not have
• AVOID using red, white and blue altogether because it will look like an Independence Day (4th of July) graphic and we dont want that

```html
<!DOCTYPE html>
<html lang="en">
<head>
<meta charset="utf-8">
<title>Copperfield Loop – The Lantern Ridge Method social graphics</title>
<link rel="stylesheet" href="https://fonts.googleapis.com/css2?family=Oswald:wght@700&family=Roboto+Slab:wght@700&family=Nunito:wght@900&family=Arimo:wght@400&display=swap">
<style>
  :root{
    --plum:#3b1450;
    --plum-deep:#230b31;
    --berry:#c42a55;
    --berry-deep:#5e1230;
    --rose:#f2a7b9;
    --blush:#f7d3d8;
    --teal:#2fae9a;
    --ink:#0d0d0d;
    --paper:#ffffff;
    --rule:#dcdcdc;
    --outfit-a:#e8435c;
    --outfit-b:#1c1c1c;
    --outfit-c:#4a3a5c;
  }
  *{box-sizing:border-box;margin:0;padding:0}
  html,body{width:1200px;height:1200px;overflow:hidden;background:var(--paper)}
  .sheet{position:relative;width:1200px;height:1200px;background:var(--paper);border:1px solid var(--rule)}

  .tile{position:absolute;width:347px;height:347px;overflow:hidden}
  .col-a{left:248px}.col-b{left:629px}
  .row-a{top:52px}.row-b{top:438px}.row-c{top:815px}

  .photo-zone{position:absolute;left:0;top:0;width:100%;height:208px}
  .band{position:absolute;left:0;top:208px;width:100%;height:139px}
  .people{position:absolute;border-radius:40% 40% 6px 6px}
  .people.pair-a{background:linear-gradient(90deg,var(--outfit-a) 0%,var(--outfit-a) 48%,var(--outfit-b) 52%,var(--outfit-b) 100%)}
  .people.pair-b{background:linear-gradient(90deg,var(--outfit-b) 0%,var(--outfit-b) 50%,var(--outfit-c) 52%,var(--outfit-c) 100%)}

  .title-top{position:absolute;font-family:"Oswald",sans-serif;font-weight:700;white-space:nowrap;line-height:1}
  .title-top .the{font-size:22px;margin-right:5px}
  .title-top .name{font-size:38px}
  .title-main{position:absolute;font-family:"Oswald",sans-serif;font-weight:700;font-size:48px;line-height:1;letter-spacing:4px;white-space:nowrap}
  .subtitle{position:absolute;font-family:"Arimo",sans-serif;font-size:21px;line-height:26px;white-space:nowrap}

  .badge{position:absolute;width:7.5em;height:5.25em}
  .badge svg{position:absolute;inset:0;width:100%;height:100%}
  .badge .shield{fill:var(--paper)}
  .badge .pill{fill:var(--pill)}
  .badge-top{position:absolute;left:0;top:0;width:100%;height:1.5em;line-height:1.5em;text-align:center;font-family:"Roboto Slab",serif;font-weight:700;font-size:1em;color:var(--pill-ink)}
  .badge-main{position:absolute;left:0;top:1.3em;width:100%;text-align:center;font-family:"Nunito",sans-serif;font-weight:900;font-size:1.55em;line-height:1.2;color:var(--today)}

  /* tile 1 – plum */
  .t1{background:var(--plum)}
  .t1 .photo-zone{background:linear-gradient(115deg,#e3f0f5 0%,#e3f0f5 42%,var(--teal) 56%,var(--rose) 66%,var(--plum) 80%)}
  .t1 .people{left:84px;top:28px;width:174px;height:180px}
  .t1 .marker{position:absolute;left:0;top:173px;width:34px;height:24px;background:var(--rose)}
  .t1 .title-top{left:45px;top:166px;color:var(--paper)}
  .t1 .title-top .the{color:var(--plum)}
  .t1 .title-main{left:20px;top:220px;color:var(--paper)}
  .t1 .subtitle{left:20px;top:278px;color:var(--paper)}
  .t1 .badge{font-size:10px;left:247px;top:23px;--pill:var(--plum);--pill-ink:var(--paper);--today:var(--plum)}

  /* tile 2 – berry */
  .t2{background:var(--berry)}
  .t2 .photo-zone{background:linear-gradient(115deg,#fbeaec 0%,#f5c9d0 45%,#e7a3b4 62%,var(--plum) 74%,var(--berry) 90%)}
  .t2 .people{left:64px;top:26px;width:220px;height:182px}
  .t2 .marker{position:absolute;left:0;top:173px;width:34px;height:24px;background:var(--ink)}
  .t2 .title-top{left:45px;top:166px;color:var(--paper)}
  .t2 .title-top .the{color:var(--berry)}
  .t2 .title-main{left:20px;top:220px;color:var(--paper)}
  .t2 .subtitle{left:18px;top:278px;color:var(--paper)}
  .t2 .badge{font-size:10px;left:247px;top:23px;--pill:var(--blush);--pill-ink:var(--plum);--today:var(--plum)}

  /* tile 3 – plum on paper */
  .t3{background:var(--paper);border:1px solid var(--rule)}
  .t3 .photo-zone{background:linear-gradient(100deg,#c497b8 0%,#8a5f92 25%,var(--plum) 50%,var(--plum) 100%)}
  .t3 .people{left:19px;top:18px;width:174px;height:190px}
  .t3 .title-top{right:26px;top:158px;color:var(--paper)}
  .t3 .title-main{left:18px;top:214px;color:var(--plum)}
  .t3 .subtitle{left:18px;top:274px;color:var(--plum)}
  .t3 .badge{font-size:13.6px;left:217px;top:60px;--pill:var(--plum);--pill-ink:var(--paper);--today:var(--plum)}

  /* tile 4 – berry on paper */
  .t4{background:var(--paper);border:1px solid var(--rule)}
  .t4 .photo-zone{background:linear-gradient(110deg,#8e2145 0%,#b0284e 40%,var(--berry) 100%)}
  .t4 .people{left:150px;top:18px;width:190px;height:190px}
  .t4 .title-top{left:20px;top:163px;color:var(--paper)}
  .t4 .title-main{left:20px;top:220px;color:var(--berry)}
  .t4 .subtitle{left:16px;top:280px;color:var(--berry)}
  .t4 .badge{font-size:13.6px;left:17px;top:59px;--pill:var(--berry);--pill-ink:var(--paper);--today:var(--berry)}

  /* tile 5 – text only, plum */
  .t5{background:var(--plum)}
  .t5 .panel{position:absolute;left:24px;top:91px;width:298px;height:256px;background:linear-gradient(180deg,var(--plum) 0%,var(--plum-deep) 100%)}
  .t5 .title-top{left:0;width:100%;text-align:center;top:128px;color:var(--paper)}
  .t5 .title-main{left:0;width:100%;text-align:center;top:176px;color:var(--paper)}
  .t5 .subtitle{left:0;width:100%;text-align:center;top:252px;color:var(--paper)}
  .t5 .badge{font-size:17px;left:109px;top:25px;--pill:var(--ink);--pill-ink:var(--paper);--today:var(--plum)}

  /* tile 6 – berry */
  .t6{background:var(--berry)}
  .t6 .panel{position:absolute;left:20px;top:97px;width:302px;height:250px;background:linear-gradient(180deg,var(--berry) 0%,var(--berry-deep) 100%)}
  .t6 .title-top{left:0;width:100%;text-align:center;top:128px;color:var(--paper)}
  .t6 .title-main{left:0;width:100%;text-align:center;top:174px;color:var(--paper)}
  .t6 .people{left:118px;top:234px;width:106px;height:113px}
  .t6 .side{position:absolute;top:236px;font-family:"Arimo",sans-serif;font-size:18px;line-height:22px;color:var(--paper)}
  .t6 .side-left{right:240px;text-align:right}
  .t6 .side-right{left:236px;text-align:left}
  .t6 .badge{font-size:17px;left:108px;top:23px;--pill:var(--ink);--pill-ink:var(--paper);--today:var(--berry)}
</style>
</head>
<body>
<main class="sheet">

  <section class="tile t1 col-a row-a">
    <div class="photo-zone"></div>
    <div class="people pair-a" role="img" aria-label="Photo of the two course hosts, woman in a pink dress and man in black, arms crossed"></div>
    <div class="band"></div>
    <div class="marker"></div>
    <h2 class="title-top"><span class="the">The</span><span class="name">Lantern Ridge</span></h2>
    <p class="title-main">METHOD</p>
    <p class="subtitle">Fast-track Your Way to<br>a Multi-Million Business!</p>
    <div class="badge">
      <svg viewBox="0 0 120 84" preserveAspectRatio="none"><path class="shield" d="M4 20Q4 13 11 13H109Q116 13 116 20V66L60 84L4 66Z"/><rect class="pill" x="14" y="0" width="92" height="24" rx="12"/></svg>
      <span class="badge-top">Sign Up</span><span class="badge-main">Today!</span>
    </div>
  </section>

  <section class="tile t2 col-b row-a">
    <div class="photo-zone"></div>
    <div class="people pair-b" role="img" aria-label="Photo of the two course hosts, man in a black turtleneck and woman in a denim jacket"></div>
    <div class="band"></div>
    <div class="marker"></div>
    <h2 class="title-top"><span class="the">The</span><span class="name">Lantern Ridge</span></h2>
    <p class="title-main">METHOD</p>
    <p class="subtitle">How to Create a 7-Figure<br>Business From Scratch</p>
    <div class="badge">
      <svg viewBox="0 0 120 84" preserveAspectRatio="none"><path class="shield" d="M4 20Q4 13 11 13H109Q116 13 116 20V66L60 84L4 66Z"/><rect class="pill" x="14" y="0" width="92" height="24" rx="12"/></svg>
      <span class="badge-top">Sign Up</span><span class="badge-main">Today!</span>
    </div>
  </section>

  <section class="tile t3 col-a row-b">
    <div class="photo-zone"></div>
    <div class="people pair-a" role="img" aria-label="Photo of the two course hosts, woman in a pink dress and man in black, arms crossed"></div>
    <h2 class="title-top"><span class="the">The</span><span class="name">Lantern Ridge</span></h2>
    <p class="title-main">METHOD</p>
    <p class="subtitle">How to Create a 7-Figure<br>Business From Scratch</p>
    <div class="badge">
      <svg viewBox="0 0 120 84" preserveAspectRatio="none"><path class="shield" d="M4 20Q4 13 11 13H109Q116 13 116 20V66L60 84L4 66Z"/><rect class="pill" x="14" y="0" width="92" height="24" rx="12"/></svg>
      <span class="badge-top">Sign Up</span><span class="badge-main">Today!</span>
    </div>
  </section>

  <section class="tile t4 col-b row-b">
    <div class="photo-zone"></div>
    <div class="people pair-b" role="img" aria-label="Photo of the two course hosts, man in a black turtleneck and woman in a denim jacket"></div>
    <h2 class="title-top"><span class="the">The</span><span class="name">Lantern Ridge</span></h2>
    <p class="title-main">METHOD</p>
    <p class="subtitle">Fast-track Your Way to<br>a Multi-Million Business!</p>
    <div class="badge">
      <svg viewBox="0 0 120 84" preserveAspectRatio="none"><path class="shield" d="M4 20Q4 13 11 13H109Q116 13 116 20V66L60 84L4 66Z"/><rect class="pill" x="14" y="0" width="92" height="24" rx="12"/></svg>
      <span class="badge-top">Sign Up</span><span class="badge-main">Today!</span>
    </div>
  </section>

  <section class="tile t5 col-a row-c">
    <div class="panel"></div>
    <h2 class="title-top"><span class="the">The</span><span class="name">Lantern Ridge</span></h2>
    <p class="title-main">METHOD</p>
    <p class="subtitle">How to Create a 7-Figure<br>Business From Scratch</p>
    <div class="badge">
      <svg viewBox="0 0 120 84" preserveAspectRatio="none"><path class="shield" d="M4 20Q4 13 11 13H109Q116 13 116 20V66L60 84L4 66Z"/><rect class="pill" x="14" y="0" width="92" height="24" rx="12"/></svg>
      <span class="badge-top">Sign Up</span><span class="badge-main">Today!</span>
    </div>
  </section>

  <section class="tile t6 col-b row-c">
    <div class="panel"></div>
    <h2 class="title-top"><span class="the">The</span><span class="name">Lantern Ridge</span></h2>
    <p class="title-main">METHOD</p>
    <div class="people pair-a" role="img" aria-label="Photo of the two course hosts, woman in a pink dress and man in black, arms crossed"></div>
    <p class="side side-left">Fast<br>Track<br>Your<br>Way</p>
    <p class="side side-right">to a<br>Multi<br>Million<br>Business!</p>
    <div class="badge">
      <svg viewBox="0 0 120 84" preserveAspectRatio="none"><path class="shield" d="M4 20Q4 13 11 13H109Q116 13 116 20V66L60 84L4 66Z"/><rect class="pill" x="14" y="0" width="92" height="24" rx="12"/></svg>
      <span class="badge-top">Sign Up</span><span class="badge-main">Today!</span>
    </div>
  </section>

</main>
</body>
</html>
```